New site design for software company, replacing current 8 year old site

The site has been up and running since 1994 getting a do-over every so often. It hasn't been updated visually since 2007.
I need a simple, clean design - The actual site content will not really change. But the dark color has to change (no more black :-)
The site is http://brinqosoft.example/ A software company publishing DLL-based, ActiveX and .NET controls for Windows.
While I like the carousel that is currently used (see ttp://brinqosoft.example/) I need new backgrounds, and overall layout, color scheme, etc.
There are just 3 basic page layouts which need to be replaced. One with the carousel header (http://brinqosoft.example), one with a small header (http://www.brinqosoft.example/Products.aspx) and one with a small header, but using the full page width (this type is not publicly accessible). The basic idea of a right pane (or left) with navigation shouldn't really be changed much, but page widths, etc. can be changed freely. (And the colors, please).
I need just html/css with the visuals (no integration, no backend, no ecommerce)

Target Market(s)

Software developers

Industry/Entity Type

Computer Software

Coding

Coded - Design and coding required

Number of Pages Required

3 page

Font styles to use
Sans Serif

Requirements
Must have
• 3 basic page layouts. One with the carousel header (http://brinqosoft.example), one with a small header (http://www.brinqosoft.example/Products.aspx) and one with a small header, but using the full page width (this type is not publicly accessible).
• NOTE: This is just for basic html/css - No other work (no integration, no backend, no ecommerce)

```html
<!DOCTYPE html>
<html lang="en">
<head>
<meta charset="utf-8">
<title>Brinqo Soft – Windows Controls</title>
<link href="https://fonts.googleapis.com/css2?family=Open+Sans:wght@400;600;700&display=swap" rel="stylesheet">
<style>
:root{
  --purple:#6e5bb0;
  --purple-light:#8f7fcc;
  --dark:#2e2e33;
  --darker:#232327;
  --text:#555;
  --muted:#888;
  --band:#efeff1;
  --line:#dcdce2;
  --white:#fff;
}
*{box-sizing:border-box;margin:0;padding:0}
html,body{width:800px;height:1200px;overflow:hidden}
body{font-family:"Open Sans",Arial,sans-serif;color:var(--text);background:#f7f7f8;font-size:7px;line-height:1.5}
a{color:inherit;text-decoration:none}
.wrap{width:740px;margin:0 auto}

/* top bar */
.topbar{height:80px;background:var(--white);display:flex;align-items:center}
.topbar .wrap{display:flex;align-items:center;justify-content:space-between}
.brand{display:flex;align-items:center;gap:6px;font-size:15px;font-weight:700;color:var(--purple)}
.brand-mark{width:12px;height:12px;background:var(--purple)}
.top-right{display:flex;align-items:center;gap:10px}
.top-links{display:flex;gap:8px;font-size:6.5px;color:var(--muted);text-transform:uppercase}
.search{width:70px;height:16px;border:1px solid var(--line);background:#fafafa}
.btn{height:18px;padding:0 12px;font-size:7px;font-weight:700;color:var(--white);display:flex;align-items:center;text-transform:uppercase}
.btn-login{background:var(--purple)}
.btn-register{background:var(--dark)}

/* nav */
.mainnav{height:17px;background:var(--dark);display:flex;align-items:center;justify-content:space-around;color:#e6e6ea;font-size:6.5px;font-weight:600;text-transform:uppercase}
.mainnav span:first-child{color:var(--white)}

/* carousel */
.hero{height:280px;background:linear-gradient(180deg,#34343a,#1f1f24);position:relative;display:flex;align-items:center}
.hero-art{position:absolute;left:40px;top:40px;width:300px;height:190px;background:linear-gradient(135deg,#d9dbe6,#8a8ea5 60%,#3a3b45);border-radius:4px}
.hero-copy{position:absolute;left:390px;top:105px;color:var(--white)}
.hero-copy h1{font-size:23px;font-weight:400;line-height:1.25}
.hero-copy h1 span{font-size:17px}
.dots{position:absolute;bottom:12px;left:0;right:0;display:flex;justify-content:center;gap:5px}
.dots i{width:6px;height:6px;border-radius:50%;background:#777;display:block}
.dots i:first-child{background:var(--white)}

/* welcome */
.welcome{background:var(--white);padding:22px 0 20px;text-align:center}
.section-title{color:var(--purple);font-size:10px;font-weight:700;text-transform:uppercase;letter-spacing:.3px}
.welcome .lead{margin:10px auto 0;width:520px;font-size:6.5px;color:var(--muted)}
.features{display:flex;gap:30px;margin-top:22px;text-align:left}
.feature{flex:1;display:flex;gap:10px}
.feature-icon{width:22px;height:22px;flex:none;border:1px solid var(--purple-light);border-radius:3px;display:flex;align-items:center;justify-content:center}
.feature h3{font-size:8px;font-weight:600;color:var(--purple)}
.feature p{font-size:6px;color:var(--muted);margin:3px 0}
.feature .more{font-size:6px;color:var(--dark);font-weight:600}

/* why */
.why{background:var(--band);padding:22px 0 24px;text-align:center;border-top:1px solid var(--line);border-bottom:1px solid var(--line)}
.why .section-title{color:var(--muted)}
.why p{margin:10px auto 0;width:640px;font-size:6.5px;color:var(--muted)}
.partners{display:flex;justify-content:center;gap:40px;margin-top:18px;align-items:center}
.partner{width:55px;height:45px;background:#cfd0d8;border-radius:4px}
.partner.round{border-radius:50%;width:45px}

/* news */
.news{padding:36px 0 22px;text-align:center}
.news-list{display:flex;gap:40px;margin-top:14px;text-align:left;border-top:1px solid var(--line);padding-top:10px}
.news-item{flex:1;display:flex;gap:8px}
.news-thumb{width:12px;height:12px;background:var(--purple);flex:none;margin-top:2px}
.news-item h4{font-size:7px;font-weight:600;color:var(--purple)}
.news-item p{font-size:6px;color:var(--muted)}
.news-item small{font-size:5.5px;color:#aaa}

/* footer */
.footer{background:var(--dark);color:#b9b9c2;height:237px;padding-top:22px}
.footer .wrap{display:flex;gap:20px}
.fcol{flex:1}
.fcol.wide{flex:1.6}
.fcol h5{font-size:7px;font-weight:700;color:var(--white);text-transform:uppercase;margin-bottom:8px}
.fcol p{font-size:6px}
.fcol ul{list-style:none;font-size:6px}
.fcol li{margin-bottom:4px}
.social{display:flex;gap:5px;margin-top:10px}
.social i{width:12px;height:12px;background:#4a4a52;display:block}
.bottombar{background:var(--darker);height:35px;color:#8e8e98;font-size:6px}
.bottombar .wrap{display:flex;justify-content:space-between;align-items:center;height:35px}
</style>
</head>
<body>
<header class="topbar">
  <div class="wrap">
    <div class="brand"><span class="brand-mark"></span>Brinqo Soft</div>
    <div class="top-right">
      <nav class="top-links"><span>Home</span><span>About</span><span>Account</span></nav>
      <div class="search"></div>
      <a class="btn btn-login">Login</a>
      <a class="btn btn-register">Register</a>
    </div>
  </div>
</header>

<div class="wrap">
  <nav class="mainnav"><span>Home</span><span>Products</span><span>Support</span><span>My Account</span><span>Purchase</span><span>About</span></nav>
  <section class="hero">
    <div class="hero-art" role="img" aria-label="Product boxes of the control libraries"></div>
    <div class="hero-copy"><h1>.NET Controls, ActiveX Controls<br><span>and DLL-Based Custom Controls</span></h1></div>
    <div class="dots"><i></i><i></i><i></i><i></i></div>
  </section>
</div>

<section class="welcome">
  <div class="wrap">
    <h2 class="section-title">Welcome to our company</h2>
    <p class="lead">We build reliable controls for Windows developers, with clear docs and direct support from the people who write the code.</p>
    <div class="features">
      <div class="feature">
        <div class="feature-icon"><svg width="12" height="12" viewBox="0 0 12 12"><rect x="1" y="1" width="10" height="10" fill="none" stroke="#6e5bb0"/></svg></div>
        <div><h3>.NET Controls</h3><p>Our .NET controls offer rich tree, tab and grid features for WinForms apps, with full designer support and samples.</p><a class="more">View All &gt;&gt;</a></div>
      </div>
      <div class="feature">
        <div class="feature-icon"><svg width="12" height="12" viewBox="0 0 12 12"><circle cx="6" cy="6" r="5" fill="none" stroke="#6e5bb0"/></svg></div>
        <div><h3>ActiveX Controls</h3><p>Our ActiveX controls work in VB6, Visual C++ and other tools that host COM, and are tested on all current Windows releases.</p><a class="more">View All &gt;&gt;</a></div>
      </div>
      <div class="feature">
        <div class="feature-icon"><svg width="12" height="12" viewBox="0 0 12 12"><path d="M2 10L6 2l4 8z" fill="none" stroke="#6e5bb0"/></svg></div>
        <div><h3>DLL Controls</h3><p>Our DLL controls are built for speed in native C and C++ projects, with small size and full source code available.</p><a class="more">View All &gt;&gt;</a></div>
      </div>
    </div>
  </div>
</section>

<section class="why">
  <div class="wrap">
    <h2 class="section-title">Why choose us?</h2>
    <p>We have served Windows developers for many years with stable, well tested controls. Our products are used in thousands of apps worldwide, and every release ships with full documentation, samples and free support by email.</p>
    <div class="partners">
      <div class="partner round"></div><div class="partner"></div><div class="partner round"></div><div class="partner"></div>
    </div>
  </div>
</section>

<section class="news">
  <div class="wrap">
    <h2 class="section-title">New products &amp; updates</h2>
    <div class="news-list">
      <div class="news-item"><span class="news-thumb"></span><div><h4>New BqTree/DLL 7.5 Released</h4><p>This release adds new themes, faster drawing and better touch input support for all tree styles.</p><small>Posted on August 20, 2015</small></div></div>
      <div class="news-item"><span class="news-thumb"></span><div><h4>New BqTabs/DLL 6.5 Released</h4><p>This update brings new tab styles, improved high DPI support and several fixes for layout.</p><small>Posted on August 14, 2015</small></div></div>
    </div>
  </div>
</section>

<footer>
  <div class="footer">
    <div class="wrap">
      <div class="fcol wide"><h5>Keep in touch</h5><p>Follow us for news on releases, updates and tips on using our controls in your own apps and tools.</p><div class="social"><i></i><i></i><i></i><i></i></div></div>
      <div class="fcol"><h5>Customer Info</h5><ul><li>My Account</li><li>Sales Requests</li><li>Subscribe</li><li>Download Products</li><li>Newsletters</li><li>Product Updates</li></ul></div>
      <div class="fcol"><h5>DLL Controls</h5><ul><li>BqBox/DLL 2.0</li><li>BqButton/DLL 2.0</li><li>BqDirectory/DLL 3.5</li><li>BqMask/DLL 5.0</li><li>BqPreview/DLL 2.0</li><li>BqTabs/DLL 6.5</li><li>BqTree/DLL 7.5</li></ul></div>
      <div class="fcol"><h5>ActiveX Controls</h5><ul><li>BqBox/OCX 3.0</li><li>BqButton/OCX 3.0</li><li>BqDirectory/OCX 3.5</li><li>BqMask/OCX 5.0</li><li>BqTabs/OCX 6.5</li><li>BqTree/OCX 7.5</li></ul></div>
      <div class="fcol"><h5>.NET Controls</h5><ul><li>BqTabs/NET 6.0</li><li>BqTree/NET 3.0</li></ul></div>
    </div>
  </div>
  <div class="bottombar">
    <div class="wrap"><span>Copyright © 2015 Brinqo Soft. All Rights Reserved.</span><span>Home | Terms of Use | Privacy Policy | Contact</span></div>
  </div>
</footer>
</body>
</html>
```